Ductless Mini Split Business Website

Amber Kite Services is looking to design an eye catching educational website about installing Ductless mini splits.

Similar to this company.
https://www.cedarcoolair.com/

```html
<!DOCTYPE html>
<html lang="en">
<head>
<meta charset="utf-8">
<title>Amber Kite Services – Ductless Experts</title>
<link href="https://fonts.googleapis.com/css2?family=Rubik:ital,wght@0,400;0,500;1,500;1,700&family=Raleway:wght@400;500;600&display=swap" rel="stylesheet">
<style>
:root{
  --yellow:#e7b50b;
  --yellow-deep:#d9a300;
  --ink:#1e1e1e;
  --text:#4a4a4a;
  --muted:#7a7a7a;
  --line:#dcdcdc;
  --footer:#262626;
  --white:#fff;
}
*{box-sizing:border-box;margin:0;padding:0}
html,body{width:1200px;height:4367px;overflow:hidden;background:var(--white)}
body{position:relative;font-family:"Raleway",sans-serif;color:var(--text);font-size:13px}
.abs{position:absolute}
h2,h3,.heading{font-family:"Rubik",sans-serif;font-weight:400;color:var(--ink)}
.btn{position:absolute;display:flex;align-items:center;justify-content:center;gap:14px;background:var(--yellow);color:var(--ink);border-radius:20px;font-size:13px;font-weight:500;height:34px}
.btn .dot{width:18px;height:18px;border-radius:50%;background:var(--ink);display:flex;align-items:center;justify-content:center}
.hex{clip-path:polygon(50% 0,100% 25%,100% 75%,50% 100%,0 75%,0 25%)}

/* header & hero */
.hero{left:0;top:0;width:1200px;height:627px;background:linear-gradient(90deg,#eaeaea,#f4f4f4 50%,#e4e4e4)}
.hero-photo{left:340px;top:120px;width:760px;height:500px;background:radial-gradient(ellipse at 50% 60%,#d9cfc6,#ebe8e5 60%,transparent 75%)}
.ac-unit{left:410px;top:130px;width:395px;height:130px;background:linear-gradient(#fff,#ececec);border-radius:10px;box-shadow:0 4px 10px rgba(0,0,0,.08)}
.hero-curve{left:0;top:560px;width:1200px;height:67px}
.logo{left:112px;top:22px;display:flex;align-items:center;gap:10px}
.logo-mark{width:34px;height:34px;border-radius:50%;background:var(--yellow)}
.logo-name{font-family:"Rubik",sans-serif;font-weight:500;font-size:20px;color:var(--ink)}
.logo-tag{left:120px;top:72px;font-family:"Rubik",sans-serif;font-weight:500;font-size:16px;color:var(--ink);letter-spacing:.5px}
.contact-top{top:16px;display:flex;gap:8px;font-size:12px;color:var(--ink);line-height:14px}
.contact-top .ic{width:26px;height:26px;border-radius:50%;display:flex;align-items:center;justify-content:center}
.nav{left:453px;top:69px;display:flex;align-items:center;gap:0;font-size:12.5px;color:var(--text)}
.nav a{color:inherit;text-decoration:none;padding:6px 19px}
.nav a.active{background:var(--yellow);color:var(--white);border-radius:16px;padding:6px 22px}
.hero-kicker{left:112px;top:256px;font-family:"Rubik",sans-serif;font-style:italic;font-weight:500;font-size:25px;color:var(--ink)}
.hero-title{left:112px;top:284px;font-family:"Rubik",sans-serif;font-style:italic;font-weight:700;font-size:46px;color:var(--ink);letter-spacing:1px}
.quote-btn{position:absolute;left:114px;top:356px;width:176px;height:34px;background:var(--ink);color:var(--white);border-radius:17px;font-size:13px;display:flex;align-items:center;justify-content:center;gap:8px}
.arrow-nav{width:28px;height:28px;border-radius:50%;background:rgba(255,255,255,.7);display:flex;align-items:center;justify-content:center;top:292px}
.badge-hex{left:578px;top:604px;width:44px;height:50px;background:var(--white);box-shadow:0 0 6px rgba(0,0,0,.15)}
.badge-hex i{position:absolute;left:12px;top:15px;width:20px;height:20px;border-radius:50%;background:var(--yellow)}

/* about */
.about-photo{left:97px;top:690px;width:395px;height:390px;background:linear-gradient(135deg,#dfe5ea,#c9b39b 55%,#f1f1f1)}
.honey-bg{left:940px;top:610px;width:260px;height:470px;background:radial-gradient(ellipse at 70% 40%,#f0f0f0,transparent 70%)}
.about-title{left:619px;top:738px;font-size:33px}
.about-rule{left:608px;top:787px;width:480px;height:2px;background:var(--ink)}
.about-text{left:619px;top:805px;width:472px;font-size:12.3px;line-height:15px;color:var(--text)}
.about-text p{margin-bottom:15px}

/* services */
.sec-title{width:1200px;left:0;text-align:center;font-size:33px}
.sec-sub{width:1200px;left:0;text-align:center;font-size:12px;color:var(--muted)}
.bee-dot{width:28px;height:28px;border-radius:50%;background:var(--yellow)}
.svc{position:absolute;width:230px;height:265px}
.svc .pic{position:absolute;inset:0}
.svc .band{position:absolute;left:0;right:0;bottom:0;height:124px;background:var(--yellow);clip-path:polygon(0 0,100% 0,100% 43%,50% 100%,0 43%);display:flex;justify-content:center;padding-top:10px;text-align:center}
.svc .band span{font-family:"Rubik",sans-serif;font-weight:500;font-size:16px;line-height:20px;color:var(--ink)}

/* financing */
.fin{left:0;top:1886px;width:1200px;height:407px;background:linear-gradient(90deg,#e6e3e0,#efedeb 45%,#f6f6f6)}
.fin-photo{left:500px;top:1886px;width:700px;height:480px;background:linear-gradient(160deg,#f3f3f3 0%,#e8d7c3 40%,#d9bfa0 65%,#f5f5f5 95%)}
.fin-kicker{left:118px;top:1968px;font-size:20px;font-family:"Rubik",sans-serif;color:var(--ink)}
.fin-title{left:112px;top:1995px;font-size:33px;font-family:"Rubik",sans-serif;font-style:italic;font-weight:500;color:var(--ink)}
.fin-rule{left:112px;top:2049px;width:370px;height:1px;background:#999}
.fin-text{left:112px;top:2060px;width:395px;font-size:12.3px;line-height:15px}
.fin-list{left:112px;top:2117px;font-size:12.5px;line-height:24px;list-style:none}
.fin-list li::before{content:"› ";font-weight:600}

/* blogs */
.card{position:absolute;top:2463px;width:307px;height:347px;border:1px solid var(--line);background:var(--white)}
.card.raised{box-shadow:0 4px 10px rgba(0,0,0,.12)}
.card .pic{height:191px}
.card .date{position:absolute;left:123px;top:160px;width:58px;height:64px;background:var(--yellow);font-family:"Rubik",sans-serif;font-size:11px;font-weight:500;color:var(--ink);display:flex;flex-direction:column;align-items:center;justify-content:center;line-height:13px}
.card h4{margin:34px 14px 10px;font-family:"Rubik",sans-serif;font-weight:500;font-size:13px;color:var(--ink)}
.card p{margin:0 14px 10px;font-size:11.5px;line-height:14px}
.card a{margin-left:14px;font-size:12px;color:var(--text)}

/* gallery */
.g{position:absolute;width:313px;height:215px}
.g-caption{position:absolute;left:16px;bottom:16px;color:var(--white);font-size:12px;line-height:15px}
.g-caption b{font-weight:500;display:block;margin-bottom:8px}
.g-caption .dot{margin-top:8px;width:16px;height:16px;border-radius:50%;background:var(--yellow)}

/* testimonials & contact */
.t-title{left:112px;top:3562px;font-size:33px}
.t-sub{left:115px;top:3605px;font-size:11.5px;color:var(--muted)}
.t-card{left:115px;top:3636px;width:460px;height:296px;border:1px solid var(--line);text-align:center}
.t-photo{position:absolute;left:170px;top:20px;width:120px;height:138px;background:linear-gradient(#eee,#e9d6b8)}
.t-name{position:absolute;top:168px;width:100%;font-family:"Rubik",sans-serif;font-size:18px;color:var(--ink)}
.t-role{position:absolute;top:190px;width:100%;font-size:13px}
.t-quote{position:absolute;top:215px;left:80px;width:300px;font-size:12.3px;line-height:15px}
.t-stars{position:absolute;top:268px;width:100%;color:var(--yellow);font-size:12px;letter-spacing:3px}
.t-dots{left:325px;top:3960px;display:flex;gap:6px}
.t-dots i{width:7px;height:7px;border-radius:50%;background:#aaa}
.t-dots i:first-child{background:var(--yellow)}
.c-title{left:654px;top:3562px;font-size:33px}
.c-sub{left:655px;top:3605px;font-size:11.5px;color:var(--muted)}
.c-box{left:624px;top:3636px;width:576px;height:335px;background:linear-gradient(90deg,var(--yellow),#efc21f)}
.worker{left:1030px;top:3575px;width:170px;height:396px;background:linear-gradient(#f2b400 0 20%,#8aa0b5 20% 70%,#4d5a66 70%)}
.field{position:absolute;background:var(--white);border:1px solid #e4d38a;font-size:12px;color:var(--muted);padding:8px 12px}
.send{left:656px;top:3910px;width:150px;height:30px;background:var(--ink);color:var(--white);border-radius:15px;font-size:13px;display:flex;align-items:center;justify-content:center}

/* footer */
.footer{left:0;top:4048px;width:1200px;height:250px;background:var(--footer);color:#ddd}
.f-logo{left:120px;top:4122px;display:flex;align-items:center;gap:10px}
.f-logo .logo-name{color:var(--yellow)}
.f-tag{left:122px;top:4168px;font-family:"Rubik",sans-serif;font-size:16px;color:var(--yellow)}
.f-head{top:4098px;font-size:16px;color:var(--white)}
.f-links{left:405px;top:4128px;list-style:none;font-size:12.5px;line-height:17.5px;color:#ddd}
.f-links li::before{content:"›  "}
.f-info{left:613px;top:4128px;font-size:12px;line-height:26px;color:#ddd}
.f-info div{display:flex;gap:18px;align-items:center}
.f-info .ic{width:14px;display:flex;justify-content:center}
.seal{left:925px;top:4130px;width:116px;height:116px;border-radius:50%;background:radial-gradient(#f3cf55,#c99500)}
.copy{left:112px;top:4326px;font-size:11.5px;color:var(--text)}
.social{left:914px;top:4318px;display:flex;gap:8px}
.social i{width:28px;height:28px;border-radius:50%;background:var(--ink)}
.social i:first-child{background:var(--yellow)}
</style>
</head>
<body>

<!-- Header / hero -->
<section class="abs hero" role="img" aria-label="Hero photo: a couple adjusting a wall-mounted mini split air conditioner in a bright room"></section>
<div class="abs hero-photo"></div>
<div class="abs ac-unit"></div>
<svg class="abs hero-curve" viewBox="0 0 1200 67" preserveAspectRatio="none"><path d="M0 12 Q600 80 1200 0 L1200 67 L0 67Z" fill="#fff"/></svg>

<div class="abs logo"><span class="logo-mark"></span><span class="logo-name">Amber Kite Services</span></div>
<div class="abs logo-tag">DUCTLESS EXPERTS</div>

<div class="abs contact-top" style="left:806px">
  <span class="ic" style="background:var(--yellow)"><svg width="12" height="12" viewBox="0 0 24 24"><path d="M6.6 10.8a15 15 0 006.6 6.6l2.2-2.2a1 1 0 011-.3 11 11 0 003.6.6 1 1 0 011 1V20a1 1 0 01-1 1A17 17 0 013 4a1 1 0 011-1h3.5a1 1 0 011 1 11 11 0 00.6 3.6 1 1 0 01-.3 1z" fill="#fff"/></svg></span>
  <div><span style="color:var(--yellow)">Call Us</span><br>123 456 7890</div>
</div>
<div class="abs contact-top" style="left:938px">
  <span class="ic" style="background:var(--ink)"><svg width="12" height="12" viewBox="0 0 24 24"><path d="M6.6 10.8a15 15 0 006.6 6.6l2.2-2.2a1 1 0 011-.3 11 11 0 003.6.6 1 1 0 011 1V20a1 1 0 01-1 1A17 17 0 013 4a1 1 0 011-1h3.5a1 1 0 011 1 11 11 0 00.6 3.6 1 1 0 01-.3 1z" fill="#fff"/></svg></span>
  <div>Email us<br>hello@amberkiteservices.com</div>
</div>

<nav class="abs nav">
  <a class="active">Home</a><a>About us</a><a>Our Services ⌄</a><a>Financing</a><a>Blogs</a><a>Gallery</a><a>Contact us</a>
</nav>

<div class="abs hero-kicker">Make Yourself</div>
<div class="abs hero-title">Comfortable</div>
<div class="quote-btn"><svg width="12" height="12" viewBox="0 0 24 24"><path d="M2 12 22 3 17 21 11 14z" fill="#fff"/></svg>Request a Quote</div>
<div class="abs arrow-nav" style="left:34px"><svg width="8" height="8" viewBox="0 0 8 8"><path d="M6 0 2 4 6 8" stroke="#333" fill="none"/></svg></div>
<div class="abs arrow-nav" style="left:1132px"><svg width="8" height="8" viewBox="0 0 8 8"><path d="M2 0 6 4 2 8" stroke="#333" fill="none"/></svg></div>
<div class="abs hex badge-hex"><i></i></div>

<!-- About -->
<div class="abs honey-bg" role="img" aria-label="Faint honeycomb background pattern"></div>
<div class="abs hex about-photo" role="img" aria-label="Photo of a technician installing a ductless indoor unit"></div>
<h2 class="abs about-title">About us</h2>
<div class="about-rule abs"></div>
<div class="abs about-text">
  <p>Lorem Ipsum is simply dummy text of the printing and typesetting industry has been the industry's standard dummy text ever since the 1500s,</p>
  <p>when an unknown printer took a galley of type and scrambled it to make a type specimen book. It has survived not only five centuries, but also the leap into electronic typesetting, remaining essentially unchanged. It was popularised in the 1960s</p>
  <p>with the release of Letraset sheets containing Lorem Ipsum passages, and more recently with desktop layout software including versions of Lorem Ipsum.</p>
</div>
<div class="btn" style="left:619px;top:1000px;width:170px">Read More <span class="dot"><svg width="8" height="8" viewBox="0 0 8 8"><path d="M2 0 6 4 2 8" stroke="#fff" fill="none" stroke-width="1.5"/></svg></span></div>

<!-- Services -->
<div class="abs bee-dot" style="left:466px;top:1160px"></div>
<h2 class="abs sec-title" style="top:1164px;padding-left:20px">Our Services</h2>
<div class="abs sec-sub" style="top:1202px;padding-left:20px">How Can We Help You?</div>

<div class="svc hex" style="left:112px;top:1254px"><div class="pic" style="background:linear-gradient(135deg,#7b7b7b,#c9c9c9)" role="img" aria-label="Photo of a baseboard heater"></div><div class="band"><span>Baseboard Heat<br>Replacement</span></div></div>
<div class="svc hex" style="left:360px;top:1254px"><div class="pic" style="background:linear-gradient(135deg,#e8e8e8,#b9a390)" role="img" aria-label="Photo of a technician installing a mini split"></div><div class="band"><span>Ductless<br>Installation</span></div></div>
<div class="svc hex" style="left:608px;top:1254px"><div class="pic" style="background:linear-gradient(135deg,#dfe3e7,#4d6a93)" role="img" aria-label="Photo of a technician repairing an indoor unit"></div><div class="band"><span>Ductless<br>Repairs</span></div></div>
<div class="svc hex" style="left:857px;top:1254px"><div class="pic" style="background:linear-gradient(#f3f3f3,#d9d4ce)" role="img" aria-label="Photo of a ceiling cassette heat pump"></div><div class="band"><span>DUCTLESS HEAT<br>PUMP</span></div></div>
<div class="svc hex" style="left:236px;top:1466px"><div class="pic" style="background:linear-gradient(135deg,#f0f0f0,#7fa4cf)" role="img" aria-label="Photo of hands cleaning a mini split filter"></div><div class="band"><span>DUCTLESS<br>MAINTENANCE</span></div></div>
<div class="svc hex" style="left:484px;top:1466px"><div class="pic" style="background:linear-gradient(#9aa2a5,#3d6b86)" role="img" aria-label="Photo of a living room with a wall unit"></div><div class="band"><span>DUCTLESS<br>WARRANTY</span></div></div>
<div class="svc hex" style="left:732px;top:1466px"><div class="pic" style="background:linear-gradient(#e4e6e8,#8d8175)" role="img" aria-label="Photo of a family relaxing at home"></div><div class="band"><span>WHOLE HOUSE<br>DUCTLESS</span></div></div>

<div class="btn" style="left:515px;top:1761px;width:170px">Read More <span class="dot"><svg width="8" height="8" viewBox="0 0 8 8"><path d="M2 0 6 4 2 8" stroke="#fff" fill="none" stroke-width="1.5"/></svg></span></div>

<!-- Financing -->
<div class="abs fin"></div>
<div class="abs fin-photo" role="img" aria-label="Photo of a smiling family lying under a wall air conditioner"></div>
<div class="abs fin-kicker">Ductless Financing</div>
<div class="abs fin-title">The Experts In Ductless</div>
<div class="abs fin-rule"></div>
<div class="abs fin-text">when an unknown printer took a galley of type and lorem scrambled it to make an&nbsp; info electronic typesetting ipsum was popularised in the 1960s.</div>
<ul class="abs fin-list"><li>Competitive Interest Rates</li><li>Secure Account &amp; Bill Payment Option Online</li></ul>
<div class="btn" style="left:108px;top:2185px;width:216px;font-size:12px;font-weight:600">APPLY FOR FINANCING</div>

<!-- Blogs -->
<h2 class="abs sec-title" style="top:2398px">Blogs</h2>
<article class="card" style="left:112px"><div class="pic" style="background:linear-gradient(135deg,#f2f2f2,#c2c7cc)" role="img" aria-label="Photo of a technician opening a wall unit"></div><div class="date hex">24<br>DEC</div><h4>What is Lorem Ipsum?</h4><p>Lorem Ipsum is simply dummy text the printing and typesetting industry Lorem Ipsum has been dummy text ever since the 1500s,</p><a>Continue..</a></article>
<article class="card raised" style="left:444px"><div class="pic" style="background:linear-gradient(135deg,#e9ecef,#9ab0c0)" role="img" aria-label="Photo of outdoor condenser units"></div><div class="date hex">24<br>DEC</div><h4>What is Lorem Ipsum?</h4><p>Lorem Ipsum is simply dummy text the printing and typesetting industry Lorem Ipsum has been dummy text ever since the 1500s,</p><a>Continue..</a></article>
<article class="card" style="left:780px"><div class="pic" style="background:linear-gradient(135deg,#eef0f2,#4a5f80)" role="img" aria-label="Photo of a technician with a clipboard"></div><div class="date hex">24<br>DEC</div><h4>What is Lorem Ipsum?</h4><p>Lorem Ipsum is simply dummy text the printing and typesetting industry Lorem Ipsum has been dummy text ever since the 1500s,</p><a>Continue..</a></article>
<div class="btn" style="left:513px;top:2841px;width:170px">View More <span class="dot"><svg width="8" height="8" viewBox="0 0 8 8"><path d="M2 0 6 4 2 8" stroke="#fff" fill="none" stroke-width="1.5"/></svg></span></div>

<!-- Gallery -->
<h2 class="abs sec-title" style="top:2905px">Gallery</h2>
<div class="g" style="left:112px;top:2968px;background:linear-gradient(#ece7e1,#6a5a4c)" role="img" aria-label="Photo of a dining room"></div>
<div class="g" style="left:442px;top:2968px;background:linear-gradient(#e9e6e2,#8c8a88)" role="img" aria-label="Photo of a woman relaxing on a sofa"></div>
<div class="g" style="left:773px;top:2968px;background:linear-gradient(#f1f0ee,#b7aea3)" role="img" aria-label="Photo of a living room with wall unit"></div>
<div class="g" style="left:112px;top:3200px;background:linear-gradient(135deg,#f2f2f2,#d8d8d8)" role="img" aria-label="Photo of a ceiling cassette unit"></div>
<div class="g" style="left:442px;top:3200px;background:linear-gradient(#5a5a5a,#2a2a2a)" role="img" aria-label="Photo of outdoor condensers"><div class="g-caption"><b>Project Title</b>Lorem Ipsum is simply dummy text type set<br>int the world industry.<div class="dot"></div></div></div>
<div class="g" style="left:773px;top:3200px;background:linear-gradient(#cfd5da,#4f6b45)" role="img" aria-label="Photo of an outdoor unit on a siding wall"></div>
<div class="abs bee-dot" style="left:492px;top:3442px;width:40px;height:40px"></div>
<div class="btn" style="left:515px;top:3441px;width:162px">View More <span class="dot"><svg width="8" height="8" viewBox="0 0 8 8"><path d="M2 0 6 4 2 8" stroke="#fff" fill="none" stroke-width="1.5"/></svg></span></div>

<!-- Testimonials -->
<h2 class="abs t-title">Testimonials</h2>
<div class="abs t-sub">What Clients say about us</div>
<div class="abs t-card">
  <div class="t-photo hex" role="img" aria-label="Portrait photo of the client"></div>
  <div class="t-name">Dana Holt</div>
  <div class="t-role">Creative Director</div>
  <div class="t-quote">Lorem Ipsum&nbsp; simply dummy text printing and typesetting industry&nbsp; simply dummy a psum is simply dummy</div>
  <div class="t-stars">★★★★★</div>
</div>
<div class="abs t-dots"><i></i><i></i><i></i></div>

<!-- Contact -->
<h2 class="abs c-title">Contact Us Today</h2>
<div class="abs c-sub">Quick Contact</div>
<div class="abs c-box"></div>
<div class="abs worker" role="img" aria-label="Photo of a smiling worker in a hard hat with a tool bag"></div>
<div class="field" style="left:656px;top:3675px;width:183px;height:36px">Name</div>
<div class="field" style="left:851px;top:3675px;width:183px;height:36px">Phone</div>
<div class="field" style="left:656px;top:3722px;width:378px;height:36px">Email</div>
<div class="field" style="left:656px;top:3770px;width:378px;height:115px">Message</div>
<div class="abs send">Send</div>

<!-- Footer -->
<footer class="abs footer"></footer>
<div class="abs f-logo"><span class="logo-mark"></span><span class="logo-name">Amber Kite Services</span></div>
<div class="abs f-tag">DUCTLESS EXPERTS</div>
<div class="abs f-head" style="left:404px">Quick Links</div>
<ul class="abs f-links"><li>Home</li><li>About us</li><li>Our Services</li><li>Financing</li><li>Blogs</li><li>FAQ</li><li>Contact us</li></ul>
<div class="abs f-head" style="left:613px">Contact information</div>
<div class="abs f-info">
  <div><span class="ic"><svg width="12" height="12" viewBox="0 0 24 24"><path d="M6.6 10.8a15 15 0 006.6 6.6l2.2-2.2a1 1 0 011-.3 11 11 0 003.6.6 1 1 0 011 1V20a1 1 0 01-1 1A17 17 0 013 4a1 1 0 011-1h3.5a1 1 0 011 1 11 11 0 00.6 3.6 1 1 0 01-.3 1z" fill="#ddd"/></svg></span>(00) 123 456 7890</div>
  <div><span class="ic"><svg width="12" height="10" viewBox="0 0 24 18"><rect width="24" height="18" fill="#ddd"/><path d="M0 0 12 10 24 0" stroke="#262626" fill="none" stroke-width="2"/></svg></span>office@amberkiteservices.com</div>
  <div><span class="ic"><svg width="10" height="14" viewBox="0 0 20 28"><path d="M10 0a10 10 0 00-10 10c0 8 10 18 10 18s10-10 10-18A10 10 0 0010 0zm0 14a4 4 0 110-8 4 4 0 010 8z" fill="#ddd"/></svg></span>480 Fernhill Road</div>
  <div><span class="ic"></span>Larkdale, KY</div>
  <div><span class="ic"></span>ZipCode : 12345</div>
</div>
<div class="abs f-head" style="left:896px">Quality Work Guarantee</div>
<div class="abs seal" role="img" aria-label="Guarantee seal"></div>

<div class="abs copy">Copyright © 2020 Amber Kite Services. All Right Reserved</div>
<div class="abs social"><i></i><i></i><i></i><i></i><i></i></div>

</body>
</html>
```